A building General Contractor is looking for a business card design

I need a business card designed. The company "Crestline Structure Builders" is a general contractor for commercial buildings and pre-engineered metal buildings.

```html
<!DOCTYPE html>
<html lang="en">
<head>
<meta charset="utf-8">
<title>Crestline Structure Builders — Business Card</title>
<link href="https://fonts.googleapis.com/css2?family=Arimo:wght@400;700&display=swap" rel="stylesheet">
<style>
  :root {
    --backdrop: #2a2a2a;
    --card: #0d0d0d;
    --card-edge: #1c1c1c;
    --ink: #f2f2f2;
    --ink-soft: #cfcfcf;
    --rule: #8a8a8a;
  }
  * { margin: 0; padding: 0; box-sizing: border-box; }
  html, body {
    width: 1200px; height: 915px; overflow: hidden;
    background: var(--backdrop);
    font-family: "Arimo", Arial, sans-serif;
    color: var(--ink);
  }
  .canvas {
    width: 1200px; height: 915px;
    display: flex; flex-direction: column;
    align-items: center; justify-content: center;
    gap: 40px;
  }
  .card {
    width: 700px; height: 400px;
    background: var(--card);
    border: 1px solid var(--card-edge);
    border-radius: 24px;
    box-shadow: 0 18px 40px rgba(0,0,0,.55);
    position: relative;
  }
  .brand {
    display: flex; align-items: center; gap: 14px;
    font-weight: 700; text-transform: uppercase;
    color: var(--ink); line-height: 1.05;
  }
  .brand-mark { width: 22px; height: 22px; background: var(--ink); flex: none; }
  .brand-name { font-size: 30px; letter-spacing: 1px; }
  .card-front { display: flex; align-items: center; justify-content: center; }
  .card-back { display: flex; align-items: center; padding: 0 48px; }
  .card-back .brand { width: 300px; }
  .card-back .brand-name { font-size: 26px; }
  .divider { width: 1px; height: 170px; background: var(--rule); margin: 0 34px; }
  .contact { display: flex; flex-direction: column; gap: 6px; }
  .person-name { font-size: 24px; font-weight: 700; letter-spacing: .5px; }
  .person-role { font-size: 15px; color: var(--ink-soft); margin-bottom: 14px; }
  .address { font-size: 15px; line-height: 1.35; margin-bottom: 10px; }
  .line { display: flex; align-items: center; gap: 8px; font-size: 15px; }
  .line svg { width: 14px; height: 14px; flex: none; }
</style>
</head>
<body>
<main class="canvas">
  <section class="card card-front">
    <div class="brand">
      <span class="brand-mark"></span>
      <span class="brand-name">Crestline<br>Structure<br>Builders</span>
    </div>
  </section>

  <section class="card card-back">
    <div class="brand">
      <span class="brand-mark"></span>
      <span class="brand-name">Crestline<br>Structure<br>Builders</span>
    </div>
    <div class="divider"></div>
    <div class="contact">
      <div class="person-name">DANIEL HARPER</div>
      <div class="person-role">Managing Director</div>
      <div class="address">58 Alder Row Suite<br>210 Fairmont, AB 51230</div>
      <div class="line">
        <svg viewBox="0 0 16 16"><path fill="#f2f2f2" d="M3 1h3l1.5 4-2 1.3a8 8 0 0 0 4.2 4.2L11 8.5l4 1.5v3a2 2 0 0 1-2 2A12 12 0 0 1 1 3a2 2 0 0 1 2-2z"/></svg>
        <span>800-555-0172</span>
      </div>
      <div class="line">
        <svg viewBox="0 0 16 16"><rect x="1" y="3" width="14" height="10" fill="#f2f2f2"/><path d="M1 3l7 6 7-6" fill="none" stroke="#0d0d0d" stroke-width="1.3"/></svg>
        <span>info@crestlinebuilders.com</span>
      </div>
      <div class="line">
        <svg viewBox="0 0 16 16"><circle cx="8" cy="8" r="7" fill="#f2f2f2"/><path d="M1 8h14M8 1c-3 3.5-3 10.5 0 14M8 1c3 3.5 3 10.5 0 14" fill="none" stroke="#0d0d0d" stroke-width="1"/></svg>
        <span>www.crestlinebuilders.com</span>
      </div>
    </div>
  </section>
</main>
</body>
</html>
```